I need a business card representing my company, VELDRA, it's an artist management and design company. Complete name is "VELDRA Artist Mgmt. + Design Co." I need it to be world class and very appealing, sophisticated and artistically unique.
Updates

Posted an updated Brief please see. I need a business card representing my company, VELDRA, it's an artist management and design company. Complete name is "VELDRA Artist Mgmt. + Design Co." I need it to be world class and very appealing, sophisticated and artistically unique.

Designs look the same

Designs look the same

Target Market(s)

Advertisers, Entertainment Companies, Commercial companies

Industry/Entity Type

Advertising

Contact Information for Business Card

I need a business card representing my company, VELDRA, it's an artist management and design company. Complete name is "VELDRA Artist Mgmt. + Design Co." I need it to be world class and very appealing, sophisticated and artistically unique. One side can be VELDRA Artist Mgmt. + Design Co. and the other my name, Teodoro Lindqvist, my contact telephone: 412.638.2957, email veldraartist@plumora.net, my address: 3264 Harwell Ave. #517 Miami, FL 33184

Font styles to use
Other font styles liked:
• Calibri

Colors
ffffff
0455a3
f37122

Requirements
Must have
• "VELDRA" stand out bigger than the rest of the text.
Nice to have
• Name "VELDRA" can be centered on one side or in the corner or along side edges, just need something cool and different.
Should not have
• I am open just try to keep it clean looking

```html
<!DOCTYPE html>
<html lang="en">
<head>
<meta charset="utf-8">
<title>VELDRA Business Card</title>
<link rel="stylesheet" href="https://fonts.googleapis.com/css2?family=Arimo:wght@400;700&family=Lato:wght@400&display=swap">
<style>
  :root {
    --backdrop: #666666;
    --card-white: #ffffff;
    --earth-brown: #6b5839;
    --ink-brown: #5a4630;
    --accent-orange: #e07f3a;
    --rule-grey: #b8b0a4;
    --text-dark: #2b2b2b;
  }
  * { margin: 0; padding: 0; box-sizing: border-box; }
  html, body {
    width: 1200px; height: 802px; overflow: hidden;
    background: var(--backdrop);
  }
  .stage { position: relative; width: 1200px; height: 802px; }
  .card {
    position: absolute; top: 274px;
    width: 443px; height: 265px;
  }
  .card--front { left: 136px; background: var(--card-white); }
  .card--back { left: 624px; background: var(--earth-brown); }

  .brand-mark {
    position: absolute; left: 38px; top: 100px;
    display: flex; align-items: center; gap: 8px;
  }
  .brand-mark__square {
    width: 14px; height: 14px; background: var(--accent-orange);
  }
  .brand-mark__name {
    font-family: "Arimo", Arial, sans-serif; font-weight: 400;
    font-size: 40px; line-height: 1; color: var(--ink-brown);
    letter-spacing: -0.5px;
  }
  .divider {
    position: absolute; left: 200px; top: 57px;
    width: 1px; height: 140px; background: var(--rule-grey);
  }
  .contact {
    position: absolute; left: 218px; top: 54px;
    font-family: "Arimo", Arial, sans-serif; color: var(--text-dark);
  }
  .contact__name {
    font-weight: 700; font-size: 14.5px; color: var(--ink-brown);
    line-height: 18px; margin-bottom: 8px;
  }
  .contact__list { list-style: none; }
  .contact__item {
    display: flex; align-items: center; gap: 4px;
    font-size: 13px; line-height: 16px;
  }
  .contact__icon { width: 13px; height: 13px; flex: none; }
  .contact__address {
    margin-top: 7px; font-size: 13px; line-height: 16px;
    font-style: normal; padding-left: 1px;
  }
  .tagline {
    position: absolute; left: 0; right: 0; top: 224px;
    text-align: center;
    font-family: "Lato", Arial, sans-serif; font-size: 13px;
    letter-spacing: 1.6px; color: var(--accent-orange);
  }
  .back-name {
    position: absolute; left: 0; right: 0; top: 106px;
    text-align: center;
    font-family: "Arimo", Arial, sans-serif; font-weight: 400;
    font-size: 48px; line-height: 1; color: var(--card-white);
  }
  .back-url {
    position: absolute; left: 0; right: 0; top: 211px;
    text-align: center;
    font-family: "Lato", Arial, sans-serif; font-size: 12px;
    letter-spacing: 1.8px; color: var(--accent-orange);
  }
</style>
</head>
<body>
<div class="stage">

  <section class="card card--front">
    <div class="brand-mark">
      <span class="brand-mark__square"></span>
      <span class="brand-mark__name">veldra</span>
    </div>
    <div class="divider"></div>
    <div class="contact">
      <p class="contact__name">TEODORO LINDQVIST</p>
      <ul class="contact__list">
        <li class="contact__item">
          <svg class="contact__icon" viewBox="0 0 13 13" aria-hidden="true"><rect width="13" height="13" rx="2.5" fill="#5a4630"/><path d="M4 3h1.8l.6 2-1 .8a5 5 0 0 0 2.3 2.3l.8-1 2 .6V10a.6.6 0 0 1-.6.6A6.6 6.6 0 0 1 3.4 3.6.6.6 0 0 1 4 3z" fill="#fff"/></svg>
          412.638.2940
        </li>
        <li class="contact__item">
          <svg class="contact__icon" viewBox="0 0 13 13" aria-hidden="true"><rect width="13" height="13" rx="2.5" fill="#5a4630"/><path d="M4 3h1.8l.6 2-1 .8a5 5 0 0 0 2.3 2.3l.8-1 2 .6V10a.6.6 0 0 1-.6.6A6.6 6.6 0 0 1 3.4 3.6.6.6 0 0 1 4 3z" fill="#fff"/></svg>
          412.638.2957 (DIRECT)
        </li>
        <li class="contact__item">
          <svg class="contact__icon" viewBox="0 0 13 13" aria-hidden="true"><rect width="13" height="13" rx="2.5" fill="#5a4630"/><rect x="4.2" y="2.6" width="4.6" height="2.4" fill="#fff"/><rect x="2.6" y="5.4" width="7.8" height="3.4" rx=".6" fill="#fff"/><rect x="4.2" y="7.6" width="4.6" height="2.8" fill="#fff" stroke="#5a4630" stroke-width=".6"/></svg>
          412.638.2948
        </li>
        <li class="contact__item">
          <svg class="contact__icon" viewBox="0 0 13 13" aria-hidden="true"><rect width="13" height="13" rx="2.5" fill="#5a4630"/><rect x="2.8" y="3.8" width="7.4" height="5.4" fill="#fff"/><path d="M2.8 3.8l3.7 3 3.7-3" fill="none" stroke="#5a4630" stroke-width=".8"/></svg>
          veldraartist@plumora.net
        </li>
        <li class="contact__item">
          <svg class="contact__icon" viewBox="0 0 13 13" aria-hidden="true"><rect width="13" height="13" rx="2.5" fill="#5a4630"/><circle cx="6.5" cy="6.5" r="3.8" fill="#fff"/><path d="M4.6 4.6l1.6.6.4 1.6-1.2 1 .4 1.6M7.6 3.2l.2 1.4 1.6.4" fill="none" stroke="#5a4630" stroke-width=".8"/></svg>
          www.veldraart.net
        </li>
      </ul>
      <address class="contact__address">Harwell Avenue Studio 517<br>Miami, Florida 33184</address>
    </div>
    <p class="tagline">ARTIST MANAGEMENT | DESIGN CO</p>
  </section>

  <section class="card card--back">
    <p class="back-name">veldra</p>
    <p class="back-url">www.veldraart.net</p>
  </section>

</div>
</body>
</html>
```